VELM Business Card

We want a fresh and clean look with a modern touch for our new business cards.
Please use our Logo and incorporate very similar colours blues/grey/white.
Logo used on back and front.
Info on back: name, email address, phone number, website, address (Banksmeadow, NSW) - please use samples for other info.
Here is website https://www.velmoro-example.de/en/
Please use our Logo and incorporate very similar colours blues/grey/white. Logo used on back and front. Info on back: name, email address, phone number, website, address (Banksmeadow, NSW) - please use samples for other info. Here is website https://www.velmoro-example.de/en/
- Matching Logo or website/catalogue

```html
<!DOCTYPE html>
<html lang="en">
<head>
<meta charset="utf-8">
<title>VELM Business Card</title>
<link href="https://fonts.googleapis.com/css2?family=Lato:wght@400;700;900&display=swap" rel="stylesheet">
<style>
  :root {
    --stage: #3a3a3c;
    --navy: #021b3f;
    --navy-soft: #0b2a57;
    --navy-deep: #011330;
    --accent: #1f7bea;
    --white: #ffffff;
    --grey: #d9dde3;
  }
  * { box-sizing: border-box; margin: 0; padding: 0; }
  html, body {
    width: 1200px; height: 689px; overflow: hidden;
    background: var(--stage);
    font-family: "Lato", sans-serif;
  }
  .stage {
    position: relative; width: 1200px; height: 689px;
    display: flex; align-items: center; justify-content: center; gap: 48px;
  }
  .card {
    position: relative; width: 540px; height: 309px;
    background: var(--navy);
    overflow: hidden;
  }
  .card-front .backdrop {
    position: absolute; inset: 0;
    background: radial-gradient(ellipse at 60% 55%, var(--navy-soft) 0%, var(--navy) 55%, var(--navy-deep) 100%);
  }
  .brand {
    position: absolute; display: flex; align-items: center; gap: 14px;
    color: var(--white); font-weight: 900; letter-spacing: 2px;
  }
  .brand .dot {
    border-radius: 50%; background: var(--accent);
  }
  .card-front .brand { left: 50%; top: 50%; transform: translate(-50%, -50%); font-size: 78px; }
  .card-front .brand .dot { width: 46px; height: 46px; }
  .card-back .brand { left: 42px; top: 50%; transform: translateY(-50%); font-size: 48px; }
  .card-back .brand .dot { width: 28px; height: 28px; }
  .divider {
    position: absolute; left: 262px; top: 56px; width: 1.5px; height: 198px;
    background: var(--accent);
  }
  .contact {
    position: absolute; left: 290px; top: 58px; color: var(--white);
  }
  .contact .name {
    color: var(--accent); font-weight: 900; font-size: 24px; letter-spacing: .5px;
    text-transform: uppercase; line-height: 1;
  }
  .contact .role { font-size: 14px; margin-top: 4px; }
  .contact ul { list-style: none; margin-top: 14px; }
  .contact li {
    display: flex; align-items: flex-start; gap: 10px;
    font-size: 13px; line-height: 18px; margin-bottom: 2px;
  }
  .contact li svg { flex: none; width: 12px; height: 12px; margin-top: 3px; fill: var(--accent); }
  .contact li.address { margin-bottom: 8px; }
</style>
</head>
<body>
<main class="stage">
  <section class="card card-front">
    <div class="backdrop" role="img" aria-label="Faint photograph of industrial bearings and gears in dark blue tones"></div>
    <div class="brand"><span class="dot"></span>VELM</div>
  </section>

  <section class="card card-back">
    <div class="brand"><span class="dot"></span>VELM</div>
    <div class="divider"></div>
    <div class="contact">
      <p class="name">Marlon Reeve</p>
      <p class="role">Founder &amp; CEO</p>
      <ul>
        <li class="address">
          <svg viewBox="0 0 12 12"><path d="M6 0a4 4 0 0 0-4 4c0 3 4 8 4 8s4-5 4-8a4 4 0 0 0-4-4zm0 5.5a1.5 1.5 0 1 1 0-3 1.5 1.5 0 0 1 0 3z"/></svg>
          <span>Lindenweg 42<br>D-48210 Oberfeld</span>
        </li>
        <li>
          <svg viewBox="0 0 12 12"><path d="M2.5 0.5l2 2.5-1 1.3a7 7 0 0 0 4.2 4.2l1.3-1 2.5 2-1.2 1.8C5.5 11.3.7 6.5.7 1.7z"/></svg>
          <span>+49 (0) 31 58 / 472 - 0</span>
        </li>
        <li>
          <svg viewBox="0 0 12 12"><path d="M3 0h6v3H3zM1 4h10v5H9v3H3V9H1zm3 3v4h4V7z"/></svg>
          <span>+49 (0) 31 58 / 472 - 150</span>
        </li>
        <li>
          <svg viewBox="0 0 12 12"><path d="M0 2h12v1L6 7 0 3zm0 2.3l6 4 6-4V10H0z"/></svg>
          <span>info@velmoro-example.de</span>
        </li>
        <li>
          <svg viewBox="0 0 12 12"><path d="M6 0a6 6 0 1 0 0 12A6 6 0 0 0 6 0zm0 1.2c.8.9 1.3 2.3 1.4 4.2H4.6C4.7 3.5 5.2 2.1 6 1.2zM4.6 6.6h2.8c-.1 1.9-.6 3.3-1.4 4.2-.8-.9-1.3-2.3-1.4-4.2z"/></svg>
          <span>www.velmoro-example.de</span>
        </li>
      </ul>
    </div>
  </section>
</main>
</body>
</html>
```